Flyer Design

I need a flyer as Iam starting a business which cleans Leather couches,sofas,chairs for residential and businesses.
We clean the interiors of automobiles and marine craft, boats large and small.
We would like to be able to get across the message that we are affordable, personal and reliable.
The Gold coast is our market and within this area there is a large amount of holiday apartments and houses which do experience high traffic to their living and dinning areas.

Target Market(s)

Target market Home,Apartment,Marine and Auto Owners

Industry/Entity Type

Residential

Requirements
Must have
• The flyer must have Company name which is PURE HIDE RESTORE MOBILE NUMBER
0431759204
EMAIL tramkell@vornexmail.com
Colours would like bright Gold or green or Red eith black lettering very modern font
Nice to have
• I would like to keep it as simple and clean looking.but eye catching
Should not have
• Dont want the flyer to look like a Real Estate flyer or a pizza advertisement.

```html
<!DOCTYPE html>
<html lang="en">
<head>
<meta charset="utf-8">
<title>Pure Hide Restore – Flyer</title>
<link rel="stylesheet" href="https://fonts.googleapis.com/css2?family=Questrial&family=Archivo+Black&family=Arimo:wght@400;700&display=swap">
<style>
  :root {
    --charcoal: #2b2b2b;
    --black: #1a1a1a;
    --gold: #f5b21e;
    --gold-deep: #e09a12;
    --title-red: #e8285a;
    --white: #ffffff;
    --tag-grey: #5a5a5a;
    --tag-grey-light: #6e6e6e;
    --green: #3cc43c;
    --purple: #9a2fc0;
    --red: #d8232a;
    --sofa-red: #c8141c;
    --room-light: #e9e4de;
    --cabin-blue: #8fb3c9;
    --cabin-light: #e6edf2;
  }
  * { margin: 0; padding: 0; box-sizing: border-box; }
  html, body { width: 932px; height: 1200px; overflow: hidden; background: var(--charcoal); }
  .flyer {
    position: relative;
    width: 932px;
    height: 1200px;
    background: var(--charcoal);
    overflow: hidden;
    font-family: "Arimo", Arial, sans-serif;
  }
  .hero-art { position: absolute; left: 0; top: 0; width: 932px; height: 580px; }
  .brand {
    position: absolute;
    right: 30px;
    top: 14px;
    text-align: right;
    font-family: "Questrial", sans-serif;
    line-height: 1;
  }
  .brand-line { display: block; font-size: 46px; letter-spacing: 1px; }
  .brand-line--top { color: var(--title-red); }
  .brand-line--bottom { color: var(--gold); margin-top: 4px; }
  .values {
    position: absolute;
    top: 645px;
    left: 0;
    width: 932px;
  }
  .value-tag {
    position: absolute;
    top: 0;
    width: 208px;
    height: 60px;
    background: linear-gradient(var(--tag-grey-light), var(--tag-grey));
    font-family: "Archivo Black", sans-serif;
    font-size: 30px;
    color: var(--black);
    display: flex;
    align-items: center;
    justify-content: center;
    clip-path: polygon(14px 0, 100% 0, 100% 100%, 0 100%, 0 14px);
  }
  .value-tag::before {
    content: "";
    position: absolute;
    inset: 0;
    border-left: 4px solid var(--accent);
    border-bottom: 4px solid var(--accent);
  }
  .value-tag::after {
    content: "";
    position: absolute;
    left: -3px; top: 5px;
    width: 22px; height: 4px;
    background: var(--accent);
    transform: rotate(-45deg);
  }
  .value-tag--personal { left: 56px; --accent: var(--green); }
  .value-tag--affordable { left: 356px; --accent: var(--purple); }
  .value-tag--reliable { left: 663px; --accent: var(--red); }
  .services {
    position: absolute;
    top: 750px;
    left: 0;
    width: 932px;
    text-align: center;
    color: var(--white);
    font-size: 23px;
    line-height: 43px;
  }
  .cabin-photo {
    position: absolute;
    left: 60px;
    top: 870px;
    width: 369px;
    height: 243px;
    background: linear-gradient(180deg, var(--cabin-light) 0%, var(--cabin-blue) 55%, #2f5f86 75%, #8a6a4a 100%);
  }
  .contact {
    position: absolute;
    left: 516px;
    width: 330px;
    height: 34px;
    border-radius: 17px;
    background: var(--gold);
    display: flex;
    align-items: center;
    color: var(--black);
    font-size: 20px;
    font-weight: 700;
  }
  .contact svg { margin-left: 26px; }
  .contact-text { flex: 1; text-align: center; padding-right: 20px; }
  .contact--phone { top: 942px; }
  .contact--email { top: 1001px; }
  .footer-band {
    position: absolute;
    left: 0; bottom: 0;
    width: 932px; height: 26px;
    background: var(--gold);
  }
</style>
</head>
<body>
<main class="flyer">
  <svg class="hero-art" viewBox="0 0 932 580" width="932" height="580">
    <defs>
      <linearGradient id="room-tone" x1="0" y1="0" x2="0" y2="1">
        <stop offset="0" stop-color="#e9e4de"/>
        <stop offset="0.45" stop-color="#d9d2ca"/>
        <stop offset="0.55" stop-color="#c8141c"/>
        <stop offset="0.8" stop-color="#9e1016"/>
        <stop offset="1" stop-color="#d8d3cd"/>
      </linearGradient>
    </defs>
    <path role="img" aria-label="Photo of a red leather three-seat sofa and armchair in a bright living room"
          d="M0 0 H932 V450 C760 470 600 560 380 548 C220 540 90 520 0 540 Z" fill="url(#room-tone)"/>
    <path d="M0 540 C90 520 220 540 380 548 C600 560 760 470 932 450 V466 C760 486 600 578 380 566 C220 558 90 540 0 560 Z" fill="var(--gold)"/>
    <path d="M476 0 H932 V128 H600 C540 128 510 80 476 0 Z" fill="var(--gold)"/>
    <path d="M486 0 H932 V120 H604 C548 120 518 76 486 0 Z" fill="var(--black)"/>
  </svg>

  <h1 class="brand">
    <span class="brand-line brand-line--top">PURE HIDE</span>
    <span class="brand-line brand-line--bottom">RESTORE</span>
  </h1>

  <ul class="values">
    <li class="value-tag value-tag--personal">Personal</li>
    <li class="value-tag value-tag--affordable">Affordable</li>
    <li class="value-tag value-tag--reliable">Reliable</li>
  </ul>

  <p class="services">
    We clean Leather couches, sofas, chairs for residential and businesses.<br>
    We clean the interiors of automobiles and marine craft, boats large and small.
  </p>

  <div class="cabin-photo" role="img" aria-label="Photo of a boat cabin interior with blue leather seating and timber floor"></div>

  <div class="contact contact--phone">
    <svg width="16" height="26" viewBox="0 0 16 26" aria-hidden="true">
      <rect x="1" y="1" width="14" height="24" rx="2" fill="var(--black)"/>
      <rect x="3" y="4" width="10" height="13" fill="var(--gold)"/>
      <circle cx="8" cy="21" r="1.6" fill="var(--gold)"/>
    </svg>
    <span class="contact-text">0431759204</span>
  </div>

  <div class="contact contact--email">
    <svg width="26" height="18" viewBox="0 0 26 18" aria-hidden="true">
      <rect x="0" y="0" width="26" height="18" fill="var(--black)"/>
      <path d="M1 1 L13 10 L25 1" fill="none" stroke="var(--gold)" stroke-width="2"/>
    </svg>
    <span class="contact-text">tramkell@vornexmail.com</span>
  </div>

  <div class="footer-band"></div>
</main>
</body>
</html>
```